hawkforge structural steel

8 1/2" x 11" flyer color both sides. Use at least 12 pictures.

Add the word; structural under HawkForge to logo

bullet points:
Laser Accuracy
On-time scheduling
Own our Equipment
39 Years Exp.
Manufacturing Construction Brackets Since 1982
We manufacture custom ibeams in Phoenix, AZ
Certified welders

Hawkforge Plant
2814 n. 17th avenue, suite-3
Phx, AZ 85019
480-629-8107

Target Market(s)

Architects, builders

Industry/Entity Type

construction

Colors
0054AA
0677BA
7BADD7
CADEEF
E8F1F8

```html
<!DOCTYPE html>
<html lang="en">
<head>
<meta charset="utf-8">
<title>HawkForge Structural Steel Flyer</title>
<link rel="stylesheet" href="https://fonts.googleapis.com/css2?family=Montserrat:wght@400;600;700&display=swap">
<style>
  :root {
    --page: #f5f5f5;
    --royal: #1555a5;
    --mid-blue: #0677ba;
    --sky: #7badd7;
    --ice: #cadeef;
    --mist: #e8f1f8;
    --navy: #1e2d4a;
    --steel-dark: #121a2a;
    --white: #ffffff;
  }
  * { box-sizing: border-box; margin: 0; padding: 0; }
  html, body { width: 1200px; height: 1200px; overflow: hidden; }
  body {
    background: var(--page);
    font-family: "Montserrat", sans-serif;
    position: relative;
  }
  .flyer {
    position: absolute;
    top: 291px;
    width: 473px;
    height: 671px;
    overflow: hidden;
    background: var(--royal);
    color: var(--white);
  }
  .flyer--solid { left: 100px; }
  .flyer--glass { left: 616px; }
  .flyer__art { position: absolute; inset: 0; width: 100%; height: 100%; }
  .brand {
    position: absolute;
    top: 58px;
    left: 250px;
    width: 200px;
    text-align: center;
  }
  .brand__mark {
    display: block;
    width: 26px;
    height: 26px;
    margin: 0 auto 10px;
    border: 2px solid var(--white);
  }
  .brand__name {
    font-size: 20px;
    font-weight: 600;
    letter-spacing: 0.5px;
    line-height: 1;
  }
  .brand__tagline {
    margin-top: 20px;
    font-size: 10px;
    font-weight: 400;
    letter-spacing: 0.2px;
  }
  .benefits {
    position: absolute;
    top: 236px;
    left: 28px;
    list-style: none;
  }
  .benefits__item {
    display: flex;
    align-items: center;
    gap: 20px;
    font-size: 17px;
    font-weight: 400;
    line-height: 21px;
    text-transform: uppercase;
    min-height: 30px;
    margin-bottom: 11px;
  }
  .benefits__item--double { margin-bottom: 7px; }
  .benefits__icon { width: 30px; height: 32px; flex: none; }
  .plant {
    position: absolute;
    top: 591px;
    left: 318px;
    font-size: 9px;
    line-height: 13px;
    font-weight: 600;
    text-transform: uppercase;
    font-style: normal;
  }
</style>
</head>
<body>
<svg width="0" height="0" style="position:absolute" aria-hidden="true">
  <defs>
    <symbol id="hex-tick" viewBox="0 0 30 32">
      <polygon points="15,1.5 28,8.5 28,23.5 15,30.5 2,23.5 2,8.5" fill="var(--white)"/>
      <polygon points="15,5.5 24.5,10.5 24.5,21.5 15,26.5 5.5,21.5 5.5,10.5" fill="var(--royal)"/>
      <path d="M9.5 16 L13.5 20 L21 11.5" fill="none" stroke="var(--white)" stroke-width="2.6" stroke-linecap="round" stroke-linejoin="round"/>
    </symbol>
    <symbol id="hex-tick-light" viewBox="0 0 30 32">
      <polygon points="15,1.5 28,8.5 28,23.5 15,30.5 2,23.5 2,8.5" fill="var(--white)"/>
      <polygon points="15,5.5 24.5,10.5 24.5,21.5 15,26.5 5.5,21.5 5.5,10.5" fill="var(--sky)"/>
      <path d="M9.5 16 L13.5 20 L21 11.5" fill="none" stroke="var(--white)" stroke-width="2.6" stroke-linecap="round" stroke-linejoin="round"/>
    </symbol>
    <linearGradient id="steel-photo" x1="0" y1="0" x2="1" y2="1">
      <stop offset="0" stop-color="#0c1424"/>
      <stop offset="0.45" stop-color="#1b3d74"/>
      <stop offset="0.8" stop-color="#214a8c"/>
      <stop offset="1" stop-color="#1e2d4a"/>
    </linearGradient>
  </defs>
</svg>

<!-- Variant one: solid -->
<section class="flyer flyer--solid">
  <svg class="flyer__art" viewBox="0 0 473 671" preserveAspectRatio="none">
    <rect width="473" height="671" fill="var(--royal)"/>
    <polygon role="img" aria-label="Photo of stacked structural steel plates fanning out" points="0,76 473,231 473,671 0,671" fill="url(#steel-photo)"/>
    <rect x="0" y="560" width="473" height="111" fill="var(--navy)" opacity="0.85"/>
  </svg>
  <div class="brand">
    <span class="brand__mark"></span>
    <div class="brand__name">HAWKFORGE</div>
    <div class="brand__tagline">STRUCTURAL UNDER HAWKFORGE</div>
  </div>
  <ul class="benefits">
    <li class="benefits__item"><svg class="benefits__icon"><use href="#hex-tick"/></svg>Laser Accuracy</li>
    <li class="benefits__item"><svg class="benefits__icon"><use href="#hex-tick"/></svg>On-time Scheduling</li>
    <li class="benefits__item"><svg class="benefits__icon"><use href="#hex-tick"/></svg>Own our Equipment</li>
    <li class="benefits__item"><svg class="benefits__icon"><use href="#hex-tick"/></svg>39 Years Exp.</li>
    <li class="benefits__item benefits__item--double"><svg class="benefits__icon"><use href="#hex-tick"/></svg><span>Manufacturing Construction<br>Brackets Since 1982</span></li>
    <li class="benefits__item benefits__item--double"><svg class="benefits__icon"><use href="#hex-tick"/></svg><span>We Manufacture Custom<br>Ibeams in Phoenix, AZ</span></li>
    <li class="benefits__item"><svg class="benefits__icon"><use href="#hex-tick"/></svg>Certified Welders</li>
  </ul>
  <address class="plant">Hawkforge Plant<br>2814 N. 17th Avenue, Suite-3<br>Phx, AZ 85019<br>480-629-8107</address>
</section>

<!-- Variant two: glass panel -->
<section class="flyer flyer--glass">
  <svg class="flyer__art" viewBox="0 0 473 671" preserveAspectRatio="none">
    <rect width="473" height="671" fill="var(--royal)"/>
    <polygon role="img" aria-label="Photo of stacked structural steel plates fanning out" points="0,76 473,231 473,671 0,671" fill="url(#steel-photo)"/>
    <rect x="-20" y="126" width="441" height="386" rx="18" fill="var(--mid-blue)" opacity="0.55"/>
    <polygon points="0,560 473,470 473,671 0,671" fill="var(--royal)"/>
    <polygon points="0,648 473,587 473,671 0,671" fill="var(--navy)"/>
  </svg>
  <div class="brand">
    <span class="brand__mark"></span>
    <div class="brand__name">HAWKFORGE</div>
    <div class="brand__tagline">STRUCTURAL UNDER HAWKFORGE</div>
  </div>
  <ul class="benefits">
    <li class="benefits__item"><svg class="benefits__icon"><use href="#hex-tick-light"/></svg>Laser Accuracy</li>
    <li class="benefits__item"><svg class="benefits__icon"><use href="#hex-tick-light"/></svg>On-time Scheduling</li>
    <li class="benefits__item"><svg class="benefits__icon"><use href="#hex-tick-light"/></svg>Own our Equipment</li>
    <li class="benefits__item"><svg class="benefits__icon"><use href="#hex-tick-light"/></svg>39 Years Exp.</li>
    <li class="benefits__item benefits__item--double"><svg class="benefits__icon"><use href="#hex-tick-light"/></svg><span>Manufacturing Construction<br>Brackets Since 1982</span></li>
    <li class="benefits__item benefits__item--double"><svg class="benefits__icon"><use href="#hex-tick-light"/></svg><span>We Manufacture Custom<br>Ibeams in Phoenix, AZ</span></li>
    <li class="benefits__item"><svg class="benefits__icon"><use href="#hex-tick-light"/></svg>Certified Welders</li>
  </ul>
  <address class="plant">Hawkforge Plant<br>2814 N. 17th Avenue, Suite-3<br>Phx, AZ 85019<br>480-629-8107</address>
</section>
</body>
</html>
```